Systems and Technology Consultants - Website

Design & Build a website for a new company which operates in the Systems and Technology space for Transportation, Government and Commercial sectors.

Overall design should be minimalist in nature.
Should also have a feed that provides news and event updates on the main page.
Logo has already been awarded and should be incorporated into the site.

We like the overall layout, functionality and simplicity of the below sites. Submitted designs could be similar to or a combination of the aspects on these sites, or perhaps a whole different concept - we are open to new ideas.
Vortrane.com
Merp.it

Update 1 Dated 27 May 2014

All I am moving away from the Merp.it website and would like it to be more aligned with Vortrane.com not only in layout but in functionality. I will be extending the deadline of this design brief for two weeks to incorporate additional requirements and will add addtional funding to the project.

Apologies for not having more information available to provide but with so many submissions its getting confusing.

Thanks Dermot
Updates

Please note that the brief has been updated and the deadline has been extended.

Important: We will need two language versions of the website, English and Arabic; the website is hosted on HostPeak

Hello All, Thank you for your submissions. We have narrowed it down to the final 6 designers and I just wanted to take a moment and provide a bit of feedback regarding the concepts that we like and the modifications we are looking for. First, let me mention some of the design functions we like. - At the top of the homepage we really like the "region" or "language" tab so that the website can be viewed in both English and Arabic. - We like the homepage to have clear color variation so that the different sections of the homepage are distinct. Additionally, we like the bottom portion of the homepage to be in red. We feel that draws attention to our contact information. Again, we would like the colors to integrate black, gray-scale, red, etc. - Having a search tab at the top of the home page, or integrated into the main image, so that the site is easy to navigate. - We especially like the main image to have the scrolling tabs at the bottom so it is easy to browse the services offered (Consultancy, Solutions Architecture, Masters Systems Integration, Independent Design Review). - In regards to the services offered tab we really like the idea that a few people presented that have the outside of our logo with an icon in the middle of consultancy, solutions, etc., etc. Secondly, as mentioned in our brief we really enjoy the design of vortrane site. Specially, we enjoy the strong iconic images they use, the way the tabs at the top scroll easily, and contact us page that generates an email. Lastly, I've included some photos of the concept we have been working on. What we are trying to demonstrate is how our company offers a range of services that are essentially linked together. We provide individual services that when combined present the full service package. We would like this concept to be integrated into the over concept of our website. Please feel free to ask for clarification of any of the above points or contact us if you have any additional questions. We appreciate all of your hard work and are very excited to see the updated designs. Best, Miriam Dowbrook Plenvaro Senior Program Manager miriam.dowbrook@plenvaro-mail.com

Industry/Entity Type

Government

Font styles to use
Serif
Sans Serif

Requirements
Must have
• Must work on/adapt to various/mobile devices (responsive)
Must be simple and straightforward
Colors should be in line/matching with logo
2 language versions: English and Arabic (no Thai)
Services should be the first group/row of items after/below the main image
Note: the website will be hosted by hostpeak
Nice to have
• Submit feedback form
What's New section
The banner at the bottom of the site should not be too large; we would like a narrow one more
It would be nice if the header/top banner (with Home, About, etc. tabs) could stay in place as you scroll down (like Vortrane and Chatterly)
We will likely only use one image with a Company slogan on the Home page rather than a carousel of images to rotate through
Should not have
• This is the existing website: http://www.plenvaro-example.org
We do not like the animation, the way the banner icons/titles bounce
Not simple enough, we don't like the functionality or how pages load so slowly
We do not like the logo centered - it should be at the left
The banner and its tabs should not be towards the right, we would like them to be centered, to go all the way across and to be below the logo

```html
<!DOCTYPE html>
<html lang="en">
<head>
<meta charset="utf-8">
<title>Plenvaro – Systems and Technology Consultants</title>
<link href="https://fonts.googleapis.com/css2?family=Open+Sans:wght@400;600;700&display=swap" rel="stylesheet">
<style>
:root{
  --red:#ef5a5f;
  --red-dark:#e0474c;
  --ink:#333;
  --muted:#777;
  --light:#f4f4f4;
  --line:#ddd;
  --white:#fff;
}
*{box-sizing:border-box;margin:0;padding:0}
html,body{width:796px;height:1200px;overflow:hidden}
body{font-family:"Open Sans",Arial,sans-serif;color:var(--ink);background:var(--white);position:relative}
.wrap{width:470px;margin:0 auto;position:relative}

/* header */
.site-header{height:93px;position:relative}
.topbar{position:absolute;top:8px;left:164px;right:164px;display:flex;justify-content:space-between;font-size:7px;color:var(--muted)}
.topbar .social{display:flex;gap:6px;align-items:center}
.topbar .social i{display:inline-block;width:7px;height:7px;border-radius:50%;background:#999}
.brand{position:absolute;left:166px;top:28px;display:flex;flex-direction:column;align-items:center;gap:4px}
.brand .mark{width:28px;height:28px;border-radius:50%;background:var(--red)}
.brand .name{font-size:10px;font-weight:700;color:var(--red);letter-spacing:1px}
.main-nav{position:absolute;top:62px;left:345px;display:flex;gap:20px;font-size:8px;color:var(--ink)}
.main-nav a{color:inherit;text-decoration:none;padding-bottom:6px}
.main-nav a.active{color:var(--red);border-bottom:2px solid var(--red)}
.rule{position:absolute;left:66px;right:66px;bottom:0;height:1px;background:var(--line)}

/* hero */
.hero{position:absolute;top:93px;left:66px;width:664px;height:363px;background:linear-gradient(180deg,#e9e9e9,#cfcfcf 60%,#bdbdbd)}
.hero-text{position:absolute;top:146px;left:114px;width:436px;text-align:center}
.hero-title{background:var(--red);color:var(--white);font-size:18px;font-weight:700;line-height:24px;padding:2px 6px}
.hero-sub{font-size:9px;color:#555;margin-top:3px;background:rgba(255,255,255,.7)}
.hero-actions{position:absolute;top:265px;left:0;right:0;display:flex;justify-content:center;gap:18px}
.btn{background:var(--red);color:var(--white);font-size:9px;padding:8px 14px;text-decoration:none;display:inline-block}
.hero-arrow{position:absolute;top:166px;width:26px;height:26px;border-radius:50%;background:var(--red);display:flex;align-items:center;justify-content:center}
.hero-arrow.prev{left:-26px;margin-left:66px}
.hero-arrow.next{right:26px}

/* services */
.intro{position:absolute;top:486px;left:150px;width:496px;text-align:center;font-size:9px;color:var(--muted);line-height:14px}
.intro b{color:var(--red);font-size:16px;font-weight:600}
.services{position:absolute;top:543px;left:170px;width:456px;display:flex;justify-content:space-between}
.service{width:76px;text-align:center;font-size:6.5px;color:var(--muted);line-height:9px}
.service .icon{width:40px;height:40px;margin:0 auto 7px;border:1px solid var(--line);background:var(--light);display:flex;align-items:center;justify-content:center}
.service .icon.on{background:var(--red);border-color:var(--red)}

/* about */
.about{position:absolute;top:650px;left:0;width:796px;height:225px;background:var(--red);color:var(--white)}
.about h2{text-align:center;font-size:16px;font-weight:400;padding-top:20px}
.about-photo{position:absolute;top:61px;left:178px;width:212px;height:132px;background:linear-gradient(135deg,#dfe4ea,#aab3bf)}
.about-copy{position:absolute;top:61px;left:411px;width:212px;font-size:7px;line-height:10px}
.about .more{position:absolute;top:178px;left:411px;border:1px solid var(--white);font-size:7px;padding:3px 8px}

/* news */
.news{position:absolute;top:875px;left:0;width:796px;height:291px;background:var(--white)}
.news h2{text-align:center;font-size:15px;font-weight:400;color:var(--red);padding-top:18px}
.news-col{position:absolute;top:58px;width:220px}
.news-col.events{left:159px}
.news-col.blog{left:411px}
.item{display:flex;gap:12px;height:62px}
.date{width:40px;height:40px;background:var(--red);color:var(--white);text-align:center;font-size:7px;font-weight:700;line-height:11px;padding-top:8px}
.date span{font-size:10px;display:block}
.thumb{width:54px;height:40px;background:linear-gradient(135deg,#c9ced4,#8f98a3);flex:none}
.item p{font-size:6.5px;line-height:9px;color:var(--muted);flex:1}
.item p b{color:var(--ink);font-weight:600;display:block}

.site-footer{position:absolute;bottom:0;left:0;width:796px;height:34px;background:var(--red);color:var(--white);font-size:7px;text-align:center;line-height:34px}
</style>
</head>
<body>
<header class="site-header">
  <div class="topbar">
    <div class="social"><i></i><i></i><i></i><span>Call Us : +1 555 0148</span></div>
    <div>Book Here | Sign In</div>
  </div>
  <div class="brand"><span class="mark"></span><span class="name">PLENVARO</span></div>
  <nav class="main-nav">
    <a class="active" href="#">Home</a><a href="#">Business unit ▾</a><a href="#">Services ▾</a><a href="#">About us</a><a href="#">Locations</a><a href="#">Contact us</a>
  </nav>
  <div class="rule"></div>
</header>

<section class="hero" role="img" aria-label="Hand holding a city skyline with an airplane overhead, greyscale">
  <div class="hero-text">
    <div class="hero-title">Plenvaro&nbsp; specializes&nbsp; in delivering quality professionalservices</div>
    <div class="hero-sub">and technical projects that support larger business goals</div>
  </div>
  <div class="hero-actions"><a class="btn" href="#">Latest Project</a><a class="btn" href="#">Quick Enquiry</a></div>
  <div class="hero-arrow prev" style="left:26px;margin:0"><svg width="10" height="10" viewBox="0 0 10 10"><path d="M7 1 3 5l4 4" fill="none" stroke="#fff" stroke-width="1.6"/></svg></div>
  <div class="hero-arrow next"><svg width="10" height="10" viewBox="0 0 10 10"><path d="M3 1l4 4-4 4" fill="none" stroke="#fff" stroke-width="1.6"/></svg></div>
</section>

<p class="intro"><b>We are</b> Plenvaro specializes in delivering quality professional services and technical projects<br>that support larger business goals.</p>

<section class="services">
  <div class="service"><div class="icon on"><svg width="16" height="16"><rect x="3" y="3" width="10" height="10" fill="none" stroke="#fff" stroke-width="1.5"/></svg></div>Systems Design &amp; Engineering</div>
  <div class="service"><div class="icon"><svg width="16" height="16"><rect x="2" y="4" width="12" height="9" fill="none" stroke="#999"/></svg></div>Systems Project Management</div>
  <div class="service"><div class="icon"><svg width="16" height="16"><path d="M3 13 13 3M8 3h5v5" fill="none" stroke="#999"/></svg></div>Trade Risk Assessment</div>
  <div class="service"><div class="icon"><svg width="16" height="16"><circle cx="8" cy="8" r="5" fill="none" stroke="#999"/></svg></div>Systems Construction Management</div>
  <div class="service"><div class="icon"><svg width="16" height="16"><path d="M8 3v10M3 8h10" stroke="#999"/></svg></div>Special Support Services</div>
</section>

<section class="about">
  <h2>About Plenvaro International</h2>
  <div class="about-photo" role="img" aria-label="Business team meeting in an office"></div>
  <p class="about-copy">Plenvaro specializes in delivering quality professional services and technical projects that support larger business goals. Our consultants work across transportation, government and commercial sectors, providing systems integration, solutions architecture and independent design review. We combine individual services into one complete package, so every client receives clear planning, careful delivery and lasting support for the systems that keep their operations moving forward every single day.</p>
  <span class="more">Read more</span>
</section>

<section class="news">
  <h2>Latest News And Blog</h2>
  <div class="news-col events">
    <div class="item"><div class="date"><span>MAY</span>20</div><p>Plenvaro joins regional transport systems forum. Our team will share lessons on integration and review of rail control projects.</p></div>
    <div class="item"><div class="date"><span>MAY</span>20</div><p>New government advisory contract signed. The work covers design review and program planning for public service systems.</p></div>
    <div class="item"><div class="date"><span>MAY</span>20</div><p>Open day at our main office. Meet the consultants and learn how our linked services support larger business goals.</p></div>
  </div>
  <div class="news-col blog">
    <div class="item"><div class="thumb" role="img" aria-label="Blog post image"></div><p><b>Blog headline goes here</b>Short notes on systems architecture and the value of clear design choices.</p></div>
    <div class="item"><div class="thumb" role="img" aria-label="Blog post image"></div><p><b>Blog headline goes here</b>How independent review helps large projects stay on time and on budget.</p></div>
    <div class="item"><div class="thumb" role="img" aria-label="Blog post image"></div><p><b>Blog headline goes here</b>A closer look at integrating new tools with existing commercial systems.</p></div>
  </div>
</section>

<footer class="site-footer">Copyright © 2014 Plenvaro International. All rights reserved.</footer>
</body>
</html>
```